Criação de Papelaria Profissional para Imóveis
" BUSCAMOS CLIENTES PARA COMERCIALIZAÇÃO E LOCAÇÃO DE BENS IMÓVEIS, BEM COMO PRESTAMOS SERVIÇOS DE ADMINISTRAÇÃO DE LOCAÇÕES. CONTUDO EMPREGAMOS E BUSCAMOS A EXCELÊNCIA E A SOFISTICAÇÃO EM NOSSA PRESTAÇÃO DE SERVIÇOS. TEMOS QUE SER DIFERENCIADOS, MUITO ACIMA DE MÉDIA E MUITO SOFISTICADOS. "

```html
<!DOCTYPE html>
<html lang="pt-BR">
<head>
<meta charset="utf-8">
<title>Valente &amp; Prado — Assinaturas de e-mail</title>
<link rel="stylesheet" href="https://fonts.googleapis.com/css2?family=Montserrat:wght@300;400;500&display=swap">
<style>
  :root {
    --bg: #2c2c2c;
    --graphite: #595959;
    --graphite-dark: #474747;
    --lime: #a8c425;
    --paper: #f3f3f3;
    --ink: #454545;
    --ink-soft: #666666;
    --white: #ffffff;
  }
  * { margin: 0; padding: 0; box-sizing: border-box; }
  html, body {
    width: 1200px; height: 1200px; overflow: hidden;
    background: var(--bg);
    font-family: "Montserrat", Arial, sans-serif;
  }
  .signature { position: absolute; left: 24px; width: 1152px; }
  .signature svg.shape { position: absolute; inset: 0; width: 100%; height: 100%; }
  .signature--vertical { top: 355px; height: 221px; }
  .signature--wave { top: 629px; height: 307px; }

  .brand { position: absolute; display: flex; align-items: center; gap: 14px; }
  .brand-mark { width: 18px; height: 18px; background: var(--lime); }
  .brand-name {
    color: var(--lime); font-weight: 400; letter-spacing: 0.08em;
    text-transform: uppercase; font-size: 22px; white-space: nowrap;
  }
  .brand-tagline {
    position: absolute; color: var(--lime); font-weight: 400;
    font-size: 13px; letter-spacing: 0.12em; text-transform: uppercase; white-space: nowrap;
  }

  .person-name { position: absolute; font-weight: 400; font-size: 26px; color: var(--ink); white-space: nowrap; }
  .person-id { position: absolute; font-weight: 400; font-size: 13px; color: var(--ink); white-space: nowrap; }

  .contact { position: absolute; list-style: none; }
  .contact li {
    display: flex; align-items: flex-start; gap: 10px;
    font-size: 16px; color: var(--ink); line-height: 1.3; white-space: nowrap;
  }
  .contact .icon {
    flex: none; width: 22px; height: 22px; border-radius: 50%;
    background: var(--lime); display: flex; align-items: center; justify-content: center;
  }
  .contact .icon svg { width: 12px; height: 12px; }
  .contact .dot { width: 8px; height: 8px; border-radius: 50%; background: var(--white); }

  /* vertical layout */
  .signature--vertical .brand { left: 40px; top: 96px; }
  .signature--vertical .brand-tagline { left: 72px; top: 134px; }
  .signature--vertical .person-name { left: 440px; top: 28px; }
  .signature--vertical .person-id { left: 440px; top: 64px; }
  .signature--vertical .contact--left { left: 440px; top: 100px; }
  .signature--vertical .contact--left li { margin-bottom: 12px; }
  .signature--vertical .contact--right { left: 786px; top: 100px; }
  .signature--vertical .contact--right li { margin-bottom: 10px; }

  /* wave layout */
  .signature--wave .brand-solo { position: absolute; left: 150px; top: 80px; width: 18px; height: 18px; background: var(--lime); }
  .signature--wave .brand-divider { position: absolute; left: 200px; top: 58px; width: 1px; height: 64px; background: var(--lime); }
  .signature--wave .brand { left: 218px; top: 70px; }
  .signature--wave .brand-name { font-size: 20px; }
  .signature--wave .brand-tagline { left: 220px; top: 102px; font-size: 12px; }
  .signature--wave .person-name { left: 720px; top: 14px; color: var(--white); font-size: 30px; font-weight: 300; }
  .signature--wave .person-id { left: 720px; top: 52px; color: var(--white); }
  .signature--wave .contact li { font-size: 15px; gap: 9px; }
  .signature--wave .contact .icon { width: 20px; height: 20px; }
  .signature--wave .contact--left { left: 576px; top: 128px; }
  .signature--wave .contact--left li { margin-bottom: 8px; }
  .signature--wave .contact--right { left: 880px; top: 132px; }
  .signature--wave .contact--right li { margin-bottom: 6px; }
</style>
</head>
<body>

<section class="signature signature--vertical" aria-label="Assinatura de e-mail, versão painel">
  <svg class="shape" viewBox="0 0 1152 221" preserveAspectRatio="none" aria-hidden="true">
    <defs>
      <linearGradient id="graphiteA" x1="0" y1="0" x2="0" y2="1">
        <stop offset="0" stop-color="#626262"/><stop offset="1" stop-color="#474747"/>
      </linearGradient>
    </defs>
    <path d="M420 0 H1100 A52 52 0 0 1 1152 52 V221 H420 Z" fill="#f3f3f3"/>
    <path d="M0 30 A30 30 0 0 1 30 0 H390 A40 40 0 0 1 430 40 V185 H0 Z" fill="url(#graphiteA)"/>
    <path d="M0 190 H430 V200 H0 Z" fill="#a8c425"/>
    <path d="M0 206 H440 C445 206 445 214 460 214 H1152 V221 H0 Z" fill="#a8c425"/>
  </svg>

  <div class="brand"><span class="brand-mark"></span><span class="brand-name">Valente &amp; Prado</span></div>
  <p class="brand-tagline">Serviços Imobiliários</p>

  <h2 class="person-name">Renato C. Arruda</h2>
  <p class="person-id">CAU A48315-2</p>

  <ul class="contact contact--left">
    <li><span class="icon"><svg viewBox="0 0 12 12"><path d="M3 1 L5 3 L4 4.5 Q5 7 7.5 8 L9 7 L11 9 L9.5 11 Q3 10 1 2.5 Z" fill="#fff"/></svg></span>+ 55 (11)90000-4521</li>
    <li><span class="icon"><svg viewBox="0 0 12 12"><rect x="1" y="3" width="10" height="7" fill="none" stroke="#fff" stroke-width="1.3"/><path d="M1 3 L6 7 L11 3" fill="none" stroke="#fff" stroke-width="1.3"/></svg></span>marinaprojetos@mailbox.com</li>
    <li><span class="icon"><span class="dot"></span></span>marinaprojetos.blogsite.com</li>
  </ul>
  <ul class="contact contact--right">
    <li><span class="icon"><span class="dot"></span></span>marina_projetos</li>
    <li><span class="icon"><svg viewBox="0 0 12 12"><path d="M6 11 C3 7 2.5 5.5 2.5 4.5 A3.5 3.5 0 0 1 9.5 4.5 C9.5 5.5 9 7 6 11 Z" fill="#fff"/></svg></span>Av. Orion 245, Beta Office<br>Torre Lisboa Sala 804<br>Cotia - SP CEP 06700000</li>
  </ul>
</section>

<section class="signature signature--wave" aria-label="Assinatura de e-mail, versão onda">
  <svg class="shape" viewBox="0 0 1152 307" preserveAspectRatio="none" aria-hidden="true">
    <defs>
      <linearGradient id="graphiteB" x1="0" y1="0" x2="0" y2="1">
        <stop offset="0" stop-color="#636363"/><stop offset="1" stop-color="#464646"/>
      </linearGradient>
    </defs>
    <path d="M0 0 H1152 V307 H70 A70 70 0 0 1 0 237 Z" fill="#f3f3f3"/>
    <path d="M0 0 H1100 A52 52 0 0 1 1152 52 V86 C900 82 720 78 540 118 C380 152 250 192 0 192 Z" fill="#a8c425"/>
    <path d="M0 0 H1100 A52 52 0 0 1 1152 52 V70 C900 66 720 62 530 102 C370 138 240 175 0 175 Z" fill="url(#graphiteB)"/>
  </svg>

  <span class="brand-solo"></span>
  <span class="brand-divider"></span>
  <div class="brand"><span class="brand-name">Valente &amp; Prado</span></div>
  <p class="brand-tagline">Serviços Imobiliários</p>

  <h2 class="person-name">Renato C. Arruda</h2>
  <p class="person-id">CAU A48315-2</p>

  <ul class="contact contact--left">
    <li><span class="icon"><svg viewBox="0 0 12 12"><path d="M3 1 L5 3 L4 4.5 Q5 7 7.5 8 L9 7 L11 9 L9.5 11 Q3 10 1 2.5 Z" fill="#fff"/></svg></span>+ 55 (11)90000-4521</li>
    <li><span class="icon"><svg viewBox="0 0 12 12"><rect x="1" y="3" width="10" height="7" fill="none" stroke="#fff" stroke-width="1.3"/><path d="M1 3 L6 7 L11 3" fill="none" stroke="#fff" stroke-width="1.3"/></svg></span>marinaprojetos@mailbox.com</li>
    <li><span class="icon"><span class="dot"></span></span>marinaprojetos.blogsite.com</li>
  </ul>
  <ul class="contact contact--right">
    <li><span class="icon"><span class="dot"></span></span>marina_projetos</li>
    <li><span class="icon"><svg viewBox="0 0 12 12"><path d="M6 11 C3 7 2.5 5.5 2.5 4.5 A3.5 3.5 0 0 1 9.5 4.5 C9.5 5.5 9 7 6 11 Z" fill="#fff"/></svg></span>Av. Orion 245, Beta Office<br>Torre Lisboa Sala 804<br>Cotia - SP CEP 06700000</li>
  </ul>
</section>

</body>
</html>
```